July 2022 Industrial Manufacturer Product Expo Mexico City

We manufacture large screws and fastners for large Mining equipment, Trains, large ships, airplanes, wind turbines, and so on. We also do custom work base on the customer needs. No matter the size we can make it.
We have a Expo coming up with companies all over the world. We have to stand out we are a family own business so our customer service will be above and beyond anyone can provide. We do not have a sales force to push our products and services we provide one on one service.
Plus@!! I'm looking for anything that you designers can come up with if it was your company to put on a business card, plus i want to do a 1 or 2 sided pamphlet, and then a website. We make Speciality Bolts for large mining equipment these bolts can be 3 to 4 foot long!!! Plus fasteners, Nuts, washers, any, size, strengths, special materials, we offer more of a ono on one customer service, We are a small company, family own, but can fulfill any type of orders. We can also provide special time lines for emergency orders. "We keep the machines running we here at RWK don't believe in down time" We want to hear any slogan based on our company to stand out.
Thanks i really appreciate all your work and options that we have to pick on. Plus just a thought we could possibly want to entertain a experience Marketing internet help maybe a employment possibility. Thanks
Updates

I need 2 cards one in Spanish and English Like the steel back ground maybe send me in some bright red and blue writing Same with the Black cards Please remove the word Military The logo RWK maybe integrate a picture of a Bolt 🔩 Thank you

Still looking for I need 2 cards one in Spanish and English Like the steel back ground maybe send me in some bright red and blue writing Same with the Black cards try bright writing Please remove the word Military The logo RWK maybe integrate a picture of a Bolt 🔩 Plus will need the company to make a brochure and website next Thank you

Target Market(s)

Large Mining, Ship, Train, Green Energy, OPRE, and Government equipment. Throughout the World

Industry/Entity Type

We can Custom Manufacture any type of Fastners for Mining equipment, Trains, Ships, Green energy, Governments, or military projects. wind turbines,

Contact Information for Business Card

I attached the name and contact info that's on a card, plus the Company Logo. Would like industrial looking background with Bright Colors that will stand out!! If we can insert somewhere maybe on back that we "Custom Manufacture Any Size or Quantity Fastners for Large Mining Equipment, Trains, Ships, Green Energy Equipment or Government Projects

Font styles to use
Other font styles liked:
• You Pick, has to be bold, colorful standout, Professional looking Beable to read it.

Colors

Designer to choose colors to be used in the design.

Requirements
Must have
• Need in Spanish and English TO STANDOUT FROM THE REST OF THE EXPO!! See Business card details, Rounded corners
Nice to have
• Can i see some of the darker cards with Bright Red and Blue letters I like to see the different type of card material, heavy thickness, plastic, transparent, Metal types, Bright Colors, I saw like Raised letters like on the logo.

```html
<!DOCTYPE html>
<html lang="es">
<head>
<meta charset="utf-8">
<title>RWK – Tarjetas de presentación</title>
<link rel="stylesheet" href="https://fonts.googleapis.com/css2?family=Quicksand:wght@500;600;700&display=swap">
<style>
  :root {
    --stage: #1c1c1e;
    --steel-dark: #8d8e92;
    --steel-mid: #b4b5b9;
    --steel-light: #eeeff1;
    --steel-edge: #a2a3a7;
    --ink-grey: #4a4b4f;
    --ink-white: #ffffff;
    --accent-blue: #1f8fe0;
    --accent-red: #e3202c;
  }
  * { box-sizing: border-box; margin: 0; padding: 0; }
  html, body {
    width: 1200px; height: 913px; overflow: hidden;
    background: var(--stage);
    font-family: "Quicksand", "Helvetica Neue", Arial, sans-serif;
  }
  .sheet {
    width: 1200px; height: 913px;
    display: flex; align-items: center; justify-content: center; gap: 50px;
  }
  .card {
    position: relative;
    width: 540px; height: 310px;
    border-radius: 38px;
    overflow: hidden;
    background:
      linear-gradient(100deg,
        var(--steel-dark) 0%,
        var(--steel-mid) 18%,
        var(--steel-dark) 30%,
        var(--steel-light) 46%,
        var(--steel-mid) 56%,
        var(--steel-light) 72%,
        var(--steel-edge) 86%,
        var(--steel-mid) 100%);
    box-shadow: 0 14px 30px rgba(0,0,0,.55);
  }
  .brand {
    font-weight: 700;
    color: var(--accent-blue);
    letter-spacing: 6px;
    display: flex; align-items: center; gap: 12px;
  }
  .brand-dot {
    width: 14px; height: 14px; border-radius: 50%;
    background: var(--accent-red);
  }

  /* Front */
  .card-front {
    display: flex; flex-direction: column; align-items: center;
    padding-top: 44px;
  }
  .card-front .brand { font-size: 58px; }
  .tagline {
    margin-top: 26px;
    text-align: center;
    color: var(--ink-grey);
    font-weight: 600;
    font-size: 17px;
    line-height: 1.5;
  }
  .tagline-lead { color: var(--accent-red); font-weight: 700; }

  /* Back */
  .card-back { padding: 34px 40px; }
  .card-back .brand {
    position: absolute; top: 34px; right: 44px;
    font-size: 48px;
  }
  .holder {
    position: absolute; left: 40px; top: 150px;
  }
  .holder-name { font-size: 21px; font-weight: 700; color: var(--ink-white); }
  .holder-role { font-size: 16px; font-weight: 700; margin-top: 2px; color: var(--accent-red); }
  .contact {
    position: absolute; left: 40px; bottom: 26px;
    list-style: none;
    color: var(--ink-white);
    font-size: 15px; font-weight: 600;
  }
  .contact li { display: flex; align-items: center; gap: 10px; line-height: 1.55; }
  .contact svg { width: 14px; height: 14px; flex: none; }
</style>
</head>
<body>
<main class="sheet">
  <section class="card card-front" aria-label="Frente de la tarjeta">
    <div class="brand"><span class="brand-dot"></span>RWK</div>
    <p class="tagline">
      <span class="tagline-lead">Custom Manufacture Any Size or</span><br>
      Quantity Fastners for Large Mining Equipment<br>
      Trains, Ships, Green Energy Equipment<br>
      or Government Projects
    </p>
  </section>

  <section class="card card-back" aria-label="Reverso de la tarjeta">
    <div class="brand"><span class="brand-dot"></span>RWK</div>
    <div class="holder">
      <p class="holder-name">Lic. Mariana Beltrán Soto</p>
      <p class="holder-role">Cotizaciones en</p>
    </div>
    <ul class="contact">
      <li>
        <svg viewBox="0 0 16 16" aria-hidden="true"><path fill="var(--accent-blue)" d="M3 1h3l1.5 4-2 1.3a9 9 0 0 0 4.2 4.2L11 8.5l4 1.5v3a2 2 0 0 1-2 2A12 12 0 0 1 1 3a2 2 0 0 1 2-2z"/></svg>
        871 555 0142
      </li>
      <li>
        <svg viewBox="0 0 16 16" aria-hidden="true"><rect x="4" y="1" width="8" height="14" rx="1.5" fill="none" stroke="var(--accent-blue)" stroke-width="1.6"/><circle cx="8" cy="12.3" r=".9" fill="var(--accent-blue)"/></svg>
        8715550187
      </li>
      <li>
        <svg viewBox="0 0 16 16" aria-hidden="true"><rect x="1" y="3" width="14" height="10" rx="1.5" fill="var(--accent-blue)"/><path d="M1.5 4l6.5 5 6.5-5" fill="none" stroke="var(--ink-white)" stroke-width="1.3"/></svg>
        pernosrwk.ventas@correo.mx
      </li>
    </ul>
  </section>
</main>
</body>
</html>
```